Atelier Mirou

I am actually making my own traditional french food.
Everything is homemade with passion.
I make differente terrines, jams, macaroons, rillettes and much more
I do as well cocktail party and catering

Hello everyone,

On the business card I would like to see appear if it's possible these following informations: traditional french food, cocktail party and catering.

```html
<!DOCTYPE html>
<html lang="en">
<head>
<meta charset="utf-8">
<title>Atelier Mirou – Business Card</title>
<link rel="stylesheet" href="https://fonts.googleapis.com/css2?family=Cinzel:wght@400;600&family=Arimo:wght@400&display=swap">
<style>
  :root {
    --page-bg: #ece6dc;
    --card-bg: #ffffff;
    --ink: #1a1a1a;
    --brand-red: #c8203a;
    --icon-blue: #2e3a8c;
    --faint: #ececec;
    --shadow: rgba(60, 40, 20, 0.18);
  }
  * { box-sizing: border-box; margin: 0; padding: 0; }
  html, body {
    width: 1088px;
    height: 1200px;
    overflow: hidden;
    background: var(--page-bg);
  }
  .sheet { position: relative; width: 1088px; height: 1200px; }
  .card {
    position: absolute;
    left: 113px;
    width: 877px;
    height: 500px;
    background: var(--card-bg);
    box-shadow: 0 4px 18px var(--shadow);
    overflow: hidden;
  }
  .card--front { top: 83px; }
  .card--back { top: 631px; }

  .brand {
    position: absolute;
    display: flex;
    align-items: center;
    gap: 14px;
    font-family: "Cinzel", serif;
    font-weight: 600;
    color: var(--ink);
    letter-spacing: 2px;
    white-space: nowrap;
  }
  .brand__dot {
    width: 18px; height: 18px;
    border-radius: 50%;
    background: var(--brand-red);
    flex: none;
  }
  .card--front .brand { left: 40px; top: 180px; font-size: 42px; }
  .card--back .brand { left: 345px; top: 320px; font-size: 44px; }

  .brand-watermark {
    position: absolute;
    right: 40px;
    top: 190px;
    font-family: "Cinzel", serif;
    font-weight: 600;
    font-size: 46px;
    letter-spacing: 2px;
    color: var(--faint);
  }

  .contact { position: absolute; left: 42px; top: 298px; }
  .contact__name {
    font-family: "Cinzel", serif;
    font-weight: 600;
    font-size: 29px;
    color: var(--brand-red);
    letter-spacing: 1px;
    margin-bottom: 22px;
  }
  .contact__line {
    display: flex;
    align-items: center;
    gap: 12px;
    font-family: "Arimo", sans-serif;
    font-size: 21px;
    color: var(--ink);
    height: 40px;
  }
  .contact__icon { width: 22px; height: 22px; flex: none; }
  .contact__abn { margin-top: 12px; }

  .services {
    position: absolute;
    left: 46px;
    top: 40px;
    list-style: none;
  }
  .services__item {
    display: flex;
    align-items: center;
    gap: 18px;
    height: 60px;
    font-family: "Cinzel", serif;
    font-size: 27px;
    color: var(--ink);
    letter-spacing: 1.5px;
  }
  .services__bullet {
    width: 10px; height: 10px;
    background: var(--brand-red);
    flex: none;
  }
</style>
</head>
<body>
<main class="sheet">
  <section class="card card--front" aria-label="Card front">
    <div class="brand-watermark" aria-hidden="true">Atelier Mirou</div>
    <div class="brand"><span class="brand__dot"></span>Atelier Mirou</div>
    <div class="contact">
      <p class="contact__name">Julien Vasseur</p>
      <p class="contact__line">
        <svg class="contact__icon" viewBox="0 0 22 22" aria-hidden="true">
          <rect width="22" height="22" rx="4" fill="var(--icon-blue)"/>
          <path d="M7 5h3l1 4-2 1.5c.8 1.6 1.9 2.7 3.5 3.5L14 12l4 1v3c0 .6-.4 1-1 1C10.4 17 5 11.6 5 6c0-.6.4-1 1-1z" fill="#fff"/>
        </svg>
        0412555318
      </p>
      <p class="contact__line">
        <svg class="contact__icon" viewBox="0 0 22 22" aria-hidden="true">
          <rect width="22" height="22" rx="4" fill="var(--icon-blue)"/>
          <rect x="4.5" y="6.5" width="13" height="9" fill="none" stroke="#fff" stroke-width="1.6"/>
          <path d="M4.5 6.5l6.5 5 6.5-5" fill="none" stroke="#fff" stroke-width="1.6"/>
        </svg>
        julien.v@exemple.fr
      </p>
      <p class="contact__line contact__abn">ABN:98715532406</p>
    </div>
  </section>

  <section class="card card--back" aria-label="Card back">
    <ul class="services">
      <li class="services__item"><span class="services__bullet"></span>Traditional French Food</li>
      <li class="services__item"><span class="services__bullet"></span>Cocktail Party</li>
      <li class="services__item"><span class="services__bullet"></span>Catering</li>
    </ul>
    <div class="brand"><span class="brand__dot"></span>Atelier Mirou</div>
  </section>
</main>
</body>
</html>
```